Brochure design

We need a 4 page A4 brochure for our engieering companyA draft version of the text can be found in the attachments, along with the logo.The text pdf shows the general style and layout of hte text, but am very open to artistic advice.Three image placeholders should be added on pages indicated - these are not yet availableThe logo gives a good idea of the colour scheme required.For background graphics, the use of swirl patterns is desirable.Look and feel should be clean and professional, not too cluttered.Final desing shoul dbe avialable in RGB psd format, with full layers so we can modify text and images easily.

```html
<!DOCTYPE html>
<html lang="en">
<head>
<meta charset="utf-8">
<title>Custom Simulation Tools</title>
<link href="https://fonts.googleapis.com/css2?family=Montserrat:wght@500;600;700;800&display=swap" rel="stylesheet">
<style>
:root{
  --teal:#3aabb3;
  --teal-deep:#2a9fa6;
  --green:#14866c;
  --navy:#28306a;
  --ink:#2c2c2c;
  --paper:#ffffff;
  --mist:#eef1f2;
}
*{margin:0;padding:0;box-sizing:border-box}
html,body{width:848px;height:1200px;overflow:hidden;background:var(--paper)}
body{font-family:'Montserrat',sans-serif;color:var(--ink);position:relative}
.page{position:relative;width:848px;height:1200px;overflow:hidden;
  background:linear-gradient(160deg,#ffffff 0%,#f4f6f7 55%,#e9edef 100%)}
.header{position:absolute;left:0;top:0;width:848px;height:290px}
.header svg{position:absolute;left:0;top:0}
.title-tab{position:absolute;left:0;top:35px;width:398px;height:41px;background:var(--mist);
  color:var(--teal-deep);font-weight:800;font-size:21px;letter-spacing:.3px;padding:8px 0 0 61px}
.intro{position:absolute;left:61px;top:90px;width:724px;color:#fff;font-weight:700;font-size:14.2px;line-height:19.5px;letter-spacing:-.1px}
.intro p{margin-bottom:11px}

.features{position:absolute;left:60px;top:281px;width:730px;display:flex;flex-direction:column;gap:15px}
.feature{display:grid;grid-template-columns:96px 1fr;column-gap:12px;align-items:start}
.feature .icon{width:96px;display:flex;align-items:center;justify-content:center}
.feature h2{font-size:16.8px;font-weight:700;line-height:21px;margin-top:-3px;letter-spacing:-.1px}
.feature ul{list-style:none;margin:3px 0 0 12px;font-size:14.2px;font-weight:500;line-height:18.5px;letter-spacing:-.2px}
.feature li{margin-bottom:5px}
.feature li:last-child{margin-bottom:0}
.f-cfd .icon{height:150px;background:var(--teal)}.f-cfd h2{color:var(--teal-deep)}
.f-thermal .icon{height:113px;background:var(--green)}.f-thermal h2{color:var(--green)}
.f-coupling .icon{height:131px;background:var(--navy)}.f-coupling h2{color:var(--navy)}

.photo{position:absolute;left:0;top:737px;width:848px;height:463px;
  background:linear-gradient(100deg,#3c5670 0%,#7a8c98 28%,#c9b79a 55%,#e8cf9c 70%,#b89670 85%,#6f6357 100%)}
</style>
</head>
<body>
<div class="page">
  <div class="header">
    <svg width="848" height="290" viewBox="0 0 848 290">
      <path d="M0 0H848V242C700 232 560 236 430 252 300 268 160 278 0 268Z" fill="#3aabb3"/>
    </svg>
    <div class="title-tab">CUSTOM SIMULATION TOOLS</div>
    <div class="intro">
      <p>Nexa have developed a simulation workflow which allows the accuracy of CFD to be exploited and integrated with thermal simulation tools. We therefore offer a more accurate analysis of machines without compromising on speed.</p>
      <p>We are motivated to improve the speed and cost effectiveness of CFD modelling for electrical machine design. Our customised tools and workflow allow the accuracy of CFD to be exploited and integrated with quicker thermal modelling tools. This allows quick design exploration and optimisation whilst maintaining accuracy.</p>
    </div>
  </div>

  <div class="features">
    <section class="feature f-cfd">
      <div class="icon">
        <svg width="76" height="76" viewBox="0 0 76 76" fill="none" stroke="#fff" stroke-width="2.4">
          <circle cx="28" cy="44" r="17" stroke-dasharray="7 4"/><circle cx="28" cy="44" r="7"/>
          <circle cx="52" cy="22" r="12" stroke-dasharray="5 3"/><circle cx="52" cy="22" r="5"/>
        </svg>
      </div>
      <div class="body">
        <h2>Customised FlowCore CFD toolset, tailored for electrical machines and electronics</h2>
        <ul>
          <li>Improved speed: minimised setup time</li>
          <li>Affordable: No expensive commercial licenses – costs don’t scale up with computing power</li>
          <li>Greater automation: Customised workflow for electrical machines; reduced user input; parameterised analysis</li>
        </ul>
      </div>
    </section>

    <section class="feature f-thermal">
      <div class="icon">
        <svg width="66" height="60" viewBox="0 0 66 60" fill="none" stroke="#fff" stroke-width="2.2">
          <rect x="3" y="3" width="60" height="42" rx="2"/><path d="M26 45v8M40 45v8M20 55h26"/>
          <path d="M10 22l8-8 8 8v12H10Z"/><path d="M34 32v-8M40 32v-14M46 32v-6M52 32v-10"/>
          <path d="M32 40l8-5 6 3 10-6"/>
        </svg>
      </div>
      <div class="body">
        <h2>Thermal modelling using our in-house thermal network tool</h2>
        <ul>
          <li>High speed design exploration to expedite the route towards design optimisation</li>
          <li>Flexible: able to simulation conventional and novel machines, as well as incor porate innovative thermal management systems</li>
          <li>In-built library of correlations for predicting flow and loss behaviour</li>
        </ul>
      </div>
    </section>

    <section class="feature f-coupling">
      <div class="icon">
        <svg width="64" height="64" viewBox="0 0 64 64" fill="none" stroke="#fff" stroke-width="2.4" stroke-linejoin="round">
          <path d="M12 6l8 8-3 3 30 30 4-1 5 6-6 6-6-5 1-4L15 19l-3 3-8-8Z"/>
          <path d="M52 6a10 10 0 0 0-12 13L8 51l5 5 32-32a10 10 0 0 0 13-12l-6 6-5-1-1-5Z"/>
        </svg>
      </div>
      <div class="body">
        <h2>Coupling between tools</h2>
        <ul>
          <li>Feed reduced order flow models from CFD into thermal networks</li>
          <li>Improved accuracy boundary conditions versus packages that rely on broad empirical correlations</li>
          <li>Ability to couple to wide range of thermal modelling packages including commercial codes</li>
        </ul>
      </div>
    </section>
  </div>

  <div class="photo" role="img" aria-label="Photo placeholder: engineers reviewing drawings and a tablet at a sunlit office desk with a hard hat"></div>
</div>
</body>
</html>
```